Business Card Design Project

Need business card for new non profit organization that includes the attached logo in some form.
with this information
Name: Michael Dorrance Pilbeam
Title: President & Founder
A: P.O. Box 51607, Portland, Oregon, 97214-5160
E: mike@dorrancetrust.org
E: mike@mikepilbeam.com
P: 1.971.555.0172

Industry/Entity Type
Non Profit

```html
<!DOCTYPE html>
<html lang="en">
<head>
<meta charset="utf-8">
<title>Dorrance Trust — Business Card</title>
<link rel="stylesheet" href="https://fonts.googleapis.com/css2?family=Cinzel:wght@400;600&family=Jost:wght@400&display=swap">
<style>
  :root {
    --navy: #2b2a6e;
    --paper: #ffffff;
    --paper-warm: #f7f5f4;
    --backdrop: #2a2a2a;
    --serif: "Cinzel", serif;
    --sans: "Jost", sans-serif;
  }
  * { box-sizing: border-box; margin: 0; padding: 0; }
  html, body { width: 1200px; height: 900px; overflow: hidden; }
  body {
    background: var(--backdrop);
    display: flex;
    flex-direction: column;
    align-items: center;
    justify-content: center;
    gap: 50px;
  }
  .card {
    position: relative;
    width: 630px;
    height: 360px;
    box-shadow: 0 10px 28px rgba(0,0,0,.55);
  }
  /* Contact side */
  .card--contact { background: var(--paper); color: var(--navy); }
  .card__rule {
    position: absolute;
    left: 0; right: 0;
    top: 172px;
    height: 2px;
    background: var(--navy);
  }
  .identity {
    position: absolute;
    left: 98px;
    top: 124px;
    text-align: right;
  }
  .identity__name {
    font-family: var(--serif);
    font-weight: 400;
    font-size: 24px;
    letter-spacing: .5px;
    line-height: 1;
  }
  .identity__title {
    font-family: var(--serif);
    font-size: 10.5px;
    letter-spacing: .3px;
    margin-top: 4px;
    text-transform: none;
  }
  .contact {
    position: absolute;
    left: 372px;
    top: 208px;
    list-style: none;
    font-family: var(--sans);
    font-size: 13.5px;
    line-height: 1.25;
  }
  .contact__item { display: flex; align-items: flex-start; gap: 10px; }
  .contact__item + .contact__item { margin-top: 1px; }
  .contact__item--address { margin-bottom: 4px; }
  .contact__icon { width: 12px; height: 12px; flex: none; margin-top: 3px; fill: var(--navy); }
  .contact__icon--pin { margin-top: 12px; }
  /* Logo side */
  .card--brand {
    background: var(--navy);
    padding: 26px;
  }
  .card__inner {
    width: 100%;
    height: 100%;
    background: var(--paper-warm);
    display: flex;
    align-items: center;
    justify-content: center;
  }
  .brand-name {
    font-family: var(--serif);
    font-weight: 600;
    font-size: 44px;
    letter-spacing: 2px;
    color: var(--navy);
  }
</style>
</head>
<body>
  <section class="card card--contact">
    <div class="identity">
      <h1 class="identity__name">Michael Dorrance Pilbeam</h1>
      <p class="identity__title">President &amp; Founder</p>
    </div>
    <div class="card__rule"></div>
    <ul class="contact">
      <li class="contact__item contact__item--address">
        <svg class="contact__icon contact__icon--pin" viewBox="0 0 12 12"><path d="M6 0a4 4 0 0 0-4 4c0 3 4 8 4 8s4-5 4-8a4 4 0 0 0-4-4zm0 5.6A1.6 1.6 0 1 1 6 2.4a1.6 1.6 0 0 1 0 3.2z"/></svg>
        <span>A: P.O. Box 51607, Portland,<br>&nbsp;&nbsp;&nbsp;&nbsp;Oregon, 97214-5160</span>
      </li>
      <li class="contact__item">
        <svg class="contact__icon" viewBox="0 0 12 12"><path d="M0 2h12v8H0z"/><path d="M0 2l6 4.5L12 2" fill="none" stroke="#fff" stroke-width="1"/></svg>
        <span>mike@dorrancetrust.org</span>
      </li>
      <li class="contact__item">
        <svg class="contact__icon" viewBox="0 0 12 12"><path d="M0 2h12v8H0z"/><path d="M0 2l6 4.5L12 2" fill="none" stroke="#fff" stroke-width="1"/></svg>
        <span>mike@mikepilbeam.com</span>
      </li>
      <li class="contact__item">
        <svg class="contact__icon" viewBox="0 0 12 12"><path d="M2.4 0.6l2 2.4-1.2 1.4c.8 1.8 2.2 3.2 4 4l1.4-1.2 2.4 2-1.4 2.2C5 11 1 7 0.4 2z"/></svg>
        <span>1.971.555.0172</span>
      </li>
    </ul>
  </section>

  <section class="card card--brand">
    <div class="card__inner">
      <p class="brand-name">Dorrance Trust</p>
    </div>
  </section>
</body>
</html>
```